**Launching Worlds Greatest Eco Friendly Doggy Poop Bags!**

We are an eco-friendly company located in San Francisco, California. We are launching a new line of amazing new eco-friendly doggy poop bags. They are biodegradable and super easy to open. Additionally they are strong, durable and light weight. We would like to see some designs for a box and logo under the label "Sunny Meadow". We'd like to see the colors green and blue used to promote earth friendly product.

Target Market(s)

Dog owners

Industry/Entity Type

It Company

Colors
00a990
0592cd
9bcb3c

Requirements
Must have
• Would like to see a happy looking dog and portray earth friendly images. Cartoon type images. Would like fun, happy, cartoon like dog and Sunny Meadow Logo to go in front of the box.
Nice to have
• Images of dog prints or happy dog(s) that we can put in different areas of the box. (examples of competitors boxes included)
Should not have
• Not fancy or formal.

```html
<!DOCTYPE html>
<html lang="en">
<head>
<meta charset="utf-8">
<title>Sunny Meadow – eco-friendly doggy poop bags</title>
<link rel="stylesheet" href="https://fonts.googleapis.com/css2?family=Rokkitt:wght@400;700&family=Courgette&family=Baloo+2:wght@600&display=swap">
<style>
  :root {
    --cream: #fcfbec;
    --band: #fdfdf3;
    --leaf-light: #e6efc9;
    --leaf-mid: #cfe3a6;
    --orange: #dd9c3c;
    --orange-soft: #e6b66c;
    --brown: #8b4528;
    --ink: #333333;
    --white: #ffffff;
    --frame: #444444;
  }
  html, body {
    margin: 0;
    padding: 0;
    overflow: hidden;
    background: var(--white);
  }
  .box-front {
    position: relative;
    width: 870px;
    height: 1200px;
    overflow: hidden;
    background: var(--cream);
    border: 1px solid var(--frame);
    box-sizing: border-box;
    font-family: "Rokkitt", Georgia, serif;
    color: var(--ink);
  }
  .leaf-pattern {
    position: absolute;
    inset: 0;
    background:
      radial-gradient(ellipse 60% 30% at 20% 15%, var(--leaf-light), transparent 70%),
      radial-gradient(ellipse 50% 35% at 85% 20%, var(--leaf-mid), transparent 70%),
      radial-gradient(ellipse 60% 30% at 30% 70%, var(--leaf-light), transparent 70%),
      radial-gradient(ellipse 50% 30% at 80% 85%, var(--leaf-mid), transparent 70%),
      var(--cream);
  }
  .size-label {
    position: absolute;
    left: 40px;
    top: 68px;
    margin: 0;
    font-size: 30px;
    line-height: 41px;
    letter-spacing: 0.5px;
  }
  .brand-band {
    position: absolute;
    left: 0;
    top: 338px;
    width: 100%;
    height: 222px;
    background: var(--band);
    display: flex;
    align-items: center;
    justify-content: center;
  }
  .brand-name {
    margin: 0;
    font-family: "Baloo 2", "Rokkitt", sans-serif;
    font-weight: 600;
    font-size: 104px;
    color: var(--brown);
    letter-spacing: 1px;
  }
  .product-pill {
    position: absolute;
    left: 169px;
    top: 598px;
    width: 535px;
    height: 55px;
    border-radius: 28px;
    background: var(--orange);
    color: var(--white);
    font-family: "Courgette", cursive;
    font-size: 33px;
    line-height: 55px;
    text-align: center;
    margin: 0;
  }
  .features {
    position: absolute;
    left: 0;
    top: 670px;
    width: 100%;
    margin: 0;
    padding: 0;
    list-style: none;
    text-align: center;
    font-size: 26px;
    line-height: 35px;
  }
  .features li::before {
    content: "❦ ";
  }
  .mascot {
    position: absolute;
    left: 552px;
    top: 778px;
    width: 210px;
    height: 245px;
    border-radius: 40% 40% 20% 20%;
    background: linear-gradient(180deg, var(--orange-soft), var(--orange) 70%, var(--brown));
  }
  .value-badge {
    position: absolute;
    left: 27px;
    top: 941px;
    width: 256px;
    height: 256px;
    border-radius: 50%;
    background: var(--orange);
    display: flex;
    align-items: center;
    justify-content: center;
  }
  .value-badge-inner {
    width: 228px;
    height: 228px;
    border-radius: 50%;
    background: var(--orange-soft);
    display: flex;
    flex-direction: column;
    align-items: center;
    justify-content: center;
    font-size: 29px;
    line-height: 34px;
    text-align: center;
  }
  .value-badge-inner strong {
    font-weight: 700;
  }
  .warning-box {
    position: absolute;
    left: 537px;
    top: 1013px;
    width: 251px;
    height: 133px;
    background: var(--orange);
    box-sizing: border-box;
    padding: 6px;
  }
  .warning-inner {
    height: 100%;
    border: 2px dashed var(--white);
    box-sizing: border-box;
    display: flex;
    flex-direction: column;
    align-items: center;
    justify-content: center;
    text-align: center;
    color: var(--ink);
    font-size: 17px;
    line-height: 22px;
  }
  .warning-title {
    font-size: 23px;
    line-height: 28px;
  }
</style>
</head>
<body>
  <main class="box-front">
    <div class="leaf-pattern" role="img" aria-label="Pale green skeleton-leaf pattern covering the background"></div>

    <p class="size-label">Standard bags<br>Sacs standards<br>Bolsas estandar</p>

    <header class="brand-band">
      <h1 class="brand-name">Sunny Meadow</h1>
    </header>

    <p class="product-pill">eco-friendly doggy poop bags.</p>

    <ul class="features">
      <li>100% eco-friendly</li>
      <li>Biodegradable and super easy to open.</li>
      <li>Strong, durable and light weight.</li>
    </ul>

    <div class="mascot" role="img" aria-label="Cartoon of a happy brown dog with a red collar standing on a small mound"></div>

    <div class="value-badge">
      <div class="value-badge-inner">
        <strong>Value Pack</strong>
        <span>Format ECONO</span>
        <span>ECONO</span>
        <span>PACK</span>
      </div>
    </div>

    <aside class="warning-box">
      <div class="warning-inner">
        <span class="warning-title">WARNING</span>
        <span>CHOKING HAZARD</span>
        <span>Please Keep away from</span>
        <span>Children</span>
      </div>
    </aside>
  </main>
</body>
</html>
```